I need a graphic for the promotion email for our "5th Yearly Crisis Preparedness Skills Camp" that incorporates our current logo and brand theme. I would like this graphic to funnel potentional attendees to register for a course. My perference would include a cool fire photo from our facility for the background. More information can be found on Marlowfieldcrew.com and also our Facebook.

```html
<!DOCTYPE html>
<html lang="en">
<head>
<meta charset="utf-8">
<title>5th Yearly Crisis Preparedness Skills Camp</title>
<link rel="stylesheet" href="https://fonts.googleapis.com/css2?family=Krona+One&family=Poppins:wght@600;700&display=swap">
<style>
  :root {
    --stage: #4b4b4b;
    --ink: #ffffff;
    --brand-red: #e3141b;
    --smoke-dark: #141414;
    --smoke-light: #3d3d3d;
    --sky-steel: #7487a0;
    --fire-orange: #d9692a;
    --ember-red: #b3121a;
    --ember-deep: #5e0a0d;
    --gear-dark: #1d2024;
    --gear-mid: #34383d;
  }
  * { margin: 0; padding: 0; box-sizing: border-box; }
  html, body { width: 1200px; height: 1001px; overflow: hidden; background: var(--stage); }
  .flyer {
    position: absolute; left: 0; top: 50px;
    width: 1200px; height: 900px; overflow: hidden;
    font-family: "Poppins", sans-serif; color: var(--ink);
  }
  .photo { position: absolute; }
  .photo-smoke { left: 0; top: 0; width: 1200px; height: 290px;
    background: radial-gradient(ellipse at 70% 30%, var(--smoke-light), var(--smoke-dark) 70%); }
  .photo-training { left: 0; top: 290px; width: 1200px; height: 293px;
    background: linear-gradient(100deg, var(--sky-steel) 0%, #8c97a6 40%, var(--fire-orange) 62%, #a7b0bc 85%); }
  .photo-hose { left: 0; top: 583px; width: 1200px; height: 317px;
    background: linear-gradient(160deg, var(--ember-deep) 0%, var(--ember-red) 45%, #8d0f14 100%); }
  .photo-instructor { left: 800px; top: 250px; width: 400px; height: 650px;
    border-radius: 180px 140px 0 0;
    background: radial-gradient(ellipse at 55% 45%, var(--gear-mid), var(--gear-dark) 70%); }

  .brand { position: absolute; left: 78px; top: 112px; display: flex; align-items: center; gap: 14px; }
  .brand-mark { width: 80px; height: 80px; flex: none; }
  .brand-name { font-family: "Poppins", sans-serif; font-weight: 600; font-size: 22px; letter-spacing: 3px; white-space: nowrap; }

  .headline { position: absolute; left: 549px; top: 88px; font-family: "Krona One", sans-serif;
    font-size: 29px; line-height: 35px; text-transform: uppercase; font-weight: 400; }
  .headline .accent { color: var(--brand-red); }
  .date-tag { position: absolute; left: 554px; top: 203px; width: 356px; height: 34px;
    background: var(--brand-red); font-family: "Krona One", sans-serif; font-size: 25px;
    line-height: 34px; text-align: center; }
  .date-tag sup { font-size: 12px; vertical-align: 12px; margin-right: 2px; }

  .classes { position: absolute; left: 100px; top: 340px; }
  .classes h2 { font-weight: 700; font-size: 27px; line-height: 40px; margin-bottom: 6px; }
  .class-list { list-style: none; }
  .class-list li { display: flex; align-items: center; gap: 6px; font-weight: 700; font-size: 23.5px; line-height: 32.5px; }
  .tick { width: 24px; height: 22px; flex: none; }

  .register { position: absolute; left: 116px; top: 650px; font-weight: 700; font-size: 25px; line-height: 33px; }
  .register .email { text-decoration: underline; text-decoration-color: var(--brand-red); text-decoration-thickness: 3px; text-underline-offset: 6px; margin-right: 10px; }
  .register .location { margin-top: 10px; }
</style>
</head>
<body>
  <main class="flyer">
    <div class="photo photo-smoke" role="img" aria-label="Dark smoke clouds rising over a treeline"></div>
    <div class="photo photo-training" role="img" aria-label="Firefighters in turnout gear spraying water at a burning industrial training structure"></div>
    <div class="photo photo-hose" role="img" aria-label="Red-tinted training ground with fire hose lines on gravel"></div>
    <div class="photo photo-instructor" role="img" aria-label="Rescue instructor in helmet and reflective turnout coat seen from behind"></div>

    <div class="brand">
      <svg class="brand-mark" viewBox="0 0 80 80" aria-hidden="true"><circle cx="40" cy="40" r="36" fill="none" stroke="#ffffff" stroke-width="3"/></svg>
      <span class="brand-name">MARLOWFIELD CREW</span>
    </div>

    <h1 class="headline">
      5th Yearly<br>
      Crisis Preparedness<br>
      <span class="accent">Skills Camp</span>
    </h1>
    <div class="date-tag">MAY 5<sup>th</sup> – 8<sup>th</sup> 2026</div>

    <section class="classes">
      <h2>AVAILABLE CLASSES:</h2>
      <ul class="class-list">
        <li><svg class="tick" viewBox="0 0 24 22"><path d="M2 12 L9 19 L22 3" fill="none" stroke="#e3141b" stroke-width="4" stroke-linecap="round"/></svg>32 Hour Exterior Fire</li>
        <li><svg class="tick" viewBox="0 0 24 22"><path d="M2 12 L9 19 L22 3" fill="none" stroke="#e3141b" stroke-width="4" stroke-linecap="round"/></svg>40 Hour Rescue Technician</li>
        <li><svg class="tick" viewBox="0 0 24 22"><path d="M2 12 L9 19 L22 3" fill="none" stroke="#e3141b" stroke-width="4" stroke-linecap="round"/></svg>40 Hour Advanced Rescue Technician (Tech Use)</li>
        <li><svg class="tick" viewBox="0 0 24 22"><path d="M2 12 L9 19 L22 3" fill="none" stroke="#e3141b" stroke-width="4" stroke-linecap="round"/></svg>40 Hours First Responder</li>
        <li><svg class="tick" viewBox="0 0 24 22"><path d="M2 12 L9 19 L22 3" fill="none" stroke="#e3141b" stroke-width="4" stroke-linecap="round"/></svg>40 Hours Hazmat Technician</li>
      </ul>
    </section>

    <section class="register">
      <p>Limited space available! Reach out to</p>
      <p><span class="email">dana@marlowfieldcrew.com</span> to register!</p>
      <p class="location">Location: Harlow Bend, TX</p>
    </section>
  </main>
</body>
</html>
```